" A empresa terá uma atuação semelhante a Verdanex, Morvatel, Tribunex, Galvo Trimesta, IRVU, Qelmo, BREMU, DOVA e KUT. O propósito desta nova empresa é apoiar empresas na evolução dos seus negócios em suas camadas estratégica, tática e operacional direcionando-as para um mercado atual e futuro, e utilizando-se de conceitos, melhores práticas globais, tendencias, tecnologias modernas e profissionais especializados. "

```html
<!DOCTYPE html>
<html lang="pt-BR">
<head>
<meta charset="utf-8">
<title>Nuvora – Cartão de visita</title>
<link href="https://fonts.googleapis.com/css2?family=Open+Sans:wght@300;400;600&display=swap" rel="stylesheet">
<style>
  :root {
    --bg: #f1f2f4;
    --card-front: #ffffff;
    --card-back: #3b4252;
    --ink: #3b4252;
    --ink-soft: #5d6370;
    --ink-faint: #9aa0ab;
    --accent: #6fa8c9;
  }
  * { margin: 0; padding: 0; box-sizing: border-box; }
  html, body { width: 1200px; height: 1200px; overflow: hidden; }
  body {
    background: var(--bg);
    font-family: "Open Sans", Arial, sans-serif;
    color: var(--ink);
    display: flex;
    flex-direction: column;
    align-items: center;
    justify-content: center;
    gap: 70px;
  }
  .card {
    width: 880px;
    height: 503px;
    border-radius: 34px;
    position: relative;
    overflow: hidden;
    box-shadow: 0 6px 22px rgba(40, 48, 64, 0.15);
  }
  .card--front { background: var(--card-front); }
  .card--back { background: var(--card-back); }

  .brand { position: absolute; left: 62px; top: 54px; display: flex; align-items: center; gap: 18px; }
  .brand__dot { width: 64px; height: 64px; border-radius: 50%; border: 6px solid var(--ink); }
  .brand__name { font-size: 58px; font-weight: 600; color: var(--ink); letter-spacing: -1px; line-height: 1; }
  .brand__tagline { position: absolute; left: 146px; top: 126px; font-size: 11px; letter-spacing: 2.5px; color: var(--ink-faint); text-transform: uppercase; }
  .brand__services { position: absolute; left: 420px; top: 60px; font-size: 12px; line-height: 1.25; letter-spacing: 1px; color: var(--ink-faint); font-weight: 600; }

  .person { position: absolute; left: 62px; top: 182px; }
  .person__name { font-size: 34px; font-weight: 400; color: var(--ink); }
  .person__role { font-size: 17px; color: var(--ink-soft); margin-top: 2px; }
  .person__contact { margin-top: 26px; font-size: 17px; color: var(--ink-soft); line-height: 1.55; }

  .company-contact { position: absolute; left: 440px; top: 300px; font-size: 16px; color: var(--ink-soft); line-height: 1.6; }
  .label { color: var(--ink); margin-right: 6px; }

  .social { position: absolute; left: 440px; top: 440px; display: flex; gap: 10px; }
  .social__item { width: 24px; height: 24px; border-radius: 50%; background: var(--ink); }

  .back-mark { position: absolute; right: 90px; bottom: 80px; display: flex; align-items: center; gap: 16px; }
  .back-mark__dot { width: 46px; height: 46px; border-radius: 50%; border: 5px solid var(--accent); }
  .back-mark__name { font-size: 44px; font-weight: 600; color: var(--accent); letter-spacing: -1px; }
</style>
</head>
<body>
  <section class="card card--front">
    <div class="brand">
      <div class="brand__dot"></div>
      <div class="brand__name">Nuvora</div>
    </div>
    <div class="brand__tagline">Rumo ao que vem</div>
    <div class="brand__services">GESTÃO<br>TECNOLOGIA<br>OUTSOURCING</div>

    <div class="person">
      <div class="person__name">Rafael Monteiro</div>
      <div class="person__role">Dept° Cargo/Função</div>
      <div class="person__contact">
        <div><span class="label">Mobile</span>(11) 98765-4321</div>
        <div><span class="label">e-mail</span>contato@nuvora.com</div>
      </div>
    </div>

    <div class="company-contact">
      <div><span class="label">Phone</span>(11) 4000-1234</div>
      <div><span class="label">Address</span>Av. Paulista Nova, 920</div>
      <div>Conj 310 - São Paulo - 04500-000</div>
      <div><span class="label">WebSite</span>www.nuvora.com.br</div>
    </div>

    <div class="social">
      <span class="social__item"></span>
      <span class="social__item"></span>
      <span class="social__item"></span>
      <span class="social__item"></span>
      <span class="social__item"></span>
    </div>
  </section>

  <section class="card card--back">
    <div class="back-mark">
      <div class="back-mark__dot"></div>
      <div class="back-mark__name">Nuvora</div>
    </div>
  </section>
</body>
</html>
```